Personnel recruitment Brunnwalder GmbH

We would like to create an attractive flyer that focuses on one of our services in Saarland and Rhineland-Palatinate. The benefits for the customer should be presented.

```html
<!DOCTYPE html>
<html lang="de">
<head>
<meta charset="utf-8">
<title>Brunnwalder GmbH – Personalvermittlung</title>
<link rel="stylesheet" href="https://fonts.googleapis.com/css2?family=Barlow:wght@800;900&family=Open+Sans:wght@800&family=Montserrat:wght@400&display=swap">
<style>
  :root {
    --teal-light: #8fd0d0;
    --teal-dark: #20a0a0;
    --ink: #111111;
    --text: #222222;
    --paper: #ffffff;
    --sky: #3e5fae;
    --facade: #b9bcc0;
  }
  * { margin: 0; padding: 0; box-sizing: border-box; }
  html, body { width: 849px; height: 1200px; overflow: hidden; background: var(--paper); }
  .flyer { position: relative; width: 849px; height: 1200px; overflow: hidden; background: var(--paper); font-family: "Montserrat", sans-serif; color: var(--text); }
  .shapes { position: absolute; inset: 0; }

  .brand { position: absolute; left: 51px; top: 78px; display: flex; align-items: center; gap: 10px; }
  .brand-square { width: 38px; height: 38px; background: var(--teal-dark); }
  .brand-name { font-family: "Barlow", sans-serif; font-weight: 800; font-size: 22px; color: var(--teal-dark); }

  .headline { position: absolute; left: 46px; top: 291px; font-family: "Barlow", sans-serif; font-weight: 900; font-size: 63px; line-height: 53px; color: var(--ink); letter-spacing: 0.5px; }
  .subline { position: absolute; left: 46px; top: 404px; font-family: "Open Sans", sans-serif; font-weight: 800; font-size: 21px; line-height: 33px; color: var(--ink); letter-spacing: 0.3px; }
  .intro { position: absolute; left: 46px; top: 473px; width: 470px; font-size: 12.6px; line-height: 19.6px; color: var(--ink); }

  .accent-line { position: absolute; left: 761px; top: 635px; width: 3px; height: 43px; background: var(--teal-light); }

  .section-title { font-family: "Barlow", sans-serif; font-weight: 800; color: var(--ink); }
  .services { position: absolute; left: 85px; top: 694px; }
  .services .section-title { font-size: 28px; line-height: 34px; }
  .service-list { list-style: none; margin-top: 6px; }
  .service-list li { position: relative; padding-left: 35px; font-size: 11.6px; line-height: 15px; min-height: 30px; margin-bottom: 12px; display: flex; align-items: center; color: var(--ink); }
  .service-list svg { position: absolute; left: 0; top: 50%; transform: translateY(-50%); }

  .benefits { position: absolute; left: 466px; top: 745px; }
  .benefits .section-title { font-size: 24px; line-height: 27px; }
  .benefit-list { list-style: none; margin-top: 7px; }
  .benefit-list li { position: relative; padding-left: 46px; font-size: 15.4px; line-height: 23px; margin-bottom: 5px; color: var(--ink); letter-spacing: 0.3px; }
  .benefit-list svg { position: absolute; left: 15px; top: 50%; transform: translateY(-50%); }

  .website { position: absolute; left: 86px; top: 1094px; font-size: 15px; color: var(--teal-light); letter-spacing: 0.4px; }
  .contact { position: absolute; left: 414px; top: 1053px; }
  .contact-call { font-size: 16px; color: var(--ink); letter-spacing: 0.2px; }
  .contact-phone { font-family: "Barlow", sans-serif; font-weight: 800; font-size: 34px; line-height: 38px; color: var(--ink); margin-left: 20px; }
  .phone-badge { position: absolute; left: 700px; top: 1059px; }
</style>
</head>
<body>
<main class="flyer">
  <svg class="shapes" width="849" height="1200" viewBox="0 0 849 1200">
    <polygon points="0,206 377,206 494,0 521,0 377,251 537,532 849,532 849,562 524,562 469,659 0,659" fill="var(--teal-light)"/>
    <defs>
      <linearGradient id="buildingTone" x1="0" y1="0" x2="0" y2="1">
        <stop offset="0" stop-color="var(--sky)"/>
        <stop offset="0.35" stop-color="#8a97b8"/>
        <stop offset="0.6" stop-color="var(--facade)"/>
        <stop offset="1" stop-color="#9a9890"/>
      </linearGradient>
    </defs>
    <polygon role="img" aria-label="Foto des Firmengebäudes mit Vorgarten und Firmenschild" points="521,0 849,0 849,512 526,512 377,251" fill="url(#buildingTone)"/>
    <polygon points="0,1056 383,1056 301,1200 0,1200" fill="var(--teal-dark)"/>
    <polygon points="414,1003 849,1003 849,1200 301,1200" fill="var(--teal-light)"/>
  </svg>

  <div class="brand">
    <span class="brand-square"></span>
    <span class="brand-name">Brunnwalder GmbH</span>
  </div>

  <h1 class="headline">PERSONAL<br>VERMITTLUNG</h1>
  <h2 class="subline">EFFIZIENTE LÖSUNGEN FÜR<br>IHRE PERSONALSUCHE</h2>
  <p class="intro">Passende Mitarbeiter zu finden, stellt heute eine große Herausforderung dar.<br>Profitieren Sie von unserem Netzwerk und unserer langjährigen Erfahrung im Recruiting.<br>Entlasten Sie Ihre Abteilungsleiter und fokussieren Sie sich auf Ihr Kerngeschäft, indem Sie uns mit der Personalvermittlung beauftragen.</p>

  <span class="accent-line"></span>

  <section class="services">
    <h3 class="section-title">UNSERE<br>DIENSTLEISTUNG</h3>
    <ul class="service-list">
      <li><svg width="21" height="21" viewBox="0 0 21 21"><circle cx="10.5" cy="10.5" r="9.5" fill="none" stroke="var(--teal-light)" stroke-width="1.2"/><path d="M6 10.8l3 3 6-6" fill="none" stroke="var(--teal-light)" stroke-width="1.3"/></svg>Erstellung des Anforderungsprofils<br>mit einem erfahrenen Recruiter</li>
      <li><svg width="21" height="21" viewBox="0 0 21 21"><circle cx="10.5" cy="10.5" r="9.5" fill="none" stroke="var(--teal-light)" stroke-width="1.2"/><path d="M6 10.8l3 3 6-6" fill="none" stroke="var(--teal-light)" stroke-width="1.3"/></svg>Gestaltung und Veröffentlichung<br>der Stellenanzeige</li>
      <li><svg width="21" height="21" viewBox="0 0 21 21"><circle cx="10.5" cy="10.5" r="9.5" fill="none" stroke="var(--teal-light)" stroke-width="1.2"/><path d="M6 10.8l3 3 6-6" fill="none" stroke="var(--teal-light)" stroke-width="1.3"/></svg>Bewerberselektion für jede<br>Qualifikation und Hierarchiestufe</li>
      <li><svg width="21" height="21" viewBox="0 0 21 21"><circle cx="10.5" cy="10.5" r="9.5" fill="none" stroke="var(--teal-light)" stroke-width="1.2"/><path d="M6 10.8l3 3 6-6" fill="none" stroke="var(--teal-light)" stroke-width="1.3"/></svg>Unterstützung beim Onboarding</li>
    </ul>
  </section>

  <section class="benefits">
    <h3 class="section-title">VORTEILE DER<br>PERSONALVERMITTLUNG</h3>
    <ul class="benefit-list">
      <li><svg width="17" height="15" viewBox="0 0 17 15"><path d="M1 8l5 5L16 1" fill="none" stroke="var(--teal-dark)" stroke-width="2.6"/></svg>Zeitersparnis und Entlastung für<br>Ihr Unternehmen</li>
      <li><svg width="17" height="15" viewBox="0 0 17 15"><path d="M1 8l5 5L16 1" fill="none" stroke="var(--teal-dark)" stroke-width="2.6"/></svg>Jahrelange Erfahrung in der<br>Rekrutierung</li>
      <li><svg width="17" height="15" viewBox="0 0 17 15"><path d="M1 8l5 5L16 1" fill="none" stroke="var(--teal-dark)" stroke-width="2.6"/></svg>Größeres Bewerbernetzwerk für<br>schnellere Ergebnisse</li>
    </ul>
  </section>

  <p class="website">www.brunnwalder.org</p>

  <div class="contact">
    <p class="contact-call">Kontaktieren Sie uns noch heute!</p>
    <p class="contact-phone">0 68 41 – 57 38 0</p>
  </div>

  <svg class="phone-badge" width="56" height="48" viewBox="0 0 56 48">
    <polygon points="14,0 42,0 56,24 42,48 14,48 0,24" fill="var(--paper)"/>
    <path d="M20 15c-1 1-1 4 1 8 3 5 7 9 12 10 2 0 3-1 4-2l-4-4-3 2c-2-1-5-4-6-6l2-3-4-5z" fill="var(--ink)"/>
    <path d="M30 15a6 6 0 0 1 5 5M31 11a10 10 0 0 1 8 8" fill="none" stroke="var(--ink)" stroke-width="1.6" stroke-linecap="round"/>
  </svg>
</main>
</body>
</html>
```